The Lindenmoor Compass Book

Cover Design for my first book. The book is for elementary school principals who are unhappy and are considering a career change but are afraid to leave. I teach them how to develop emotional fitness and resiliency through thought management so that they can decide whether to stay or leave their position from a place of empowerment. I've attached my podcast artwork for your reference. My publisher suggested not having me on the cover which is fine. I just thought it might be helpful.

Target Market(s)

Elementary School Principals

Industry/Entity Type

Education

Logo Text

The Lindenmoor Compass

Font styles to use
Serif
Sans Serif

Colors
34a6d7
33b8a4
3276b5

Requirements
Must have
• Title, Author name, photo or artwork that captures the essence of the book

```html
<!DOCTYPE html>
<html lang="en">
<head>
<meta charset="utf-8">
<title>The Lindenmoor Compass — Book Cover</title>
<link rel="stylesheet" href="https://fonts.googleapis.com/css2?family=Montserrat:wght@300;900&family=Oswald:wght@400;600&display=swap">
<style>
  :root {
    --backdrop: #555555;
    --cover: #f6f6f6;
    --ink-dark: #1a1a1a;
    --title-wine: #5a1222;
    --art-violet: #3c2f78;
    --art-plum: #5b2354;
    --art-wine: #7d1a2c;
    --art-teal: #66b3b0;
    --art-navy: #2a2a5e;
  }
  * { margin: 0; padding: 0; box-sizing: border-box; }
  html, body {
    width: 1198px;
    height: 1200px;
    overflow: hidden;
    background: var(--backdrop);
  }
  .book-cover {
    position: absolute;
    left: 149px;
    top: 15px;
    width: 900px;
    height: 1170px;
    background: var(--cover);
  }
  .cover-title {
    position: absolute;
    left: 0;
    top: 0;
    width: 900px;
    height: 1000px;
  }
  .title-lead {
    font-family: "Montserrat", sans-serif;
    font-weight: 300;
    fill: var(--title-wine);
  }
  .title-block {
    font-family: "Montserrat", sans-serif;
    font-weight: 900;
  }
  .title-tail {
    font-family: "Montserrat", sans-serif;
    font-weight: 300;
  }
  .author-line {
    position: absolute;
    left: 0;
    width: 900px;
    top: 1082px;
    text-align: center;
    font-family: "Oswald", sans-serif;
    color: var(--ink-dark);
    font-size: 36px;
    letter-spacing: 0.5px;
    line-height: 1;
  }
  .author-line .author-with {
    font-weight: 400;
    font-size: 30px;
    margin-right: 6px;
  }
  .author-line .author-name {
    font-weight: 600;
  }
</style>
</head>
<body>
  <main class="book-cover">
    <svg class="cover-title" viewBox="0 0 900 1000" xmlns="http://www.w3.org/2000/svg" role="img"
         aria-label="Book title set in heavy letters filled with a painted portrait of a woman in violet, wine-red and teal tones">
      <defs>
        <linearGradient id="artFill" gradientUnits="userSpaceOnUse" x1="150" y1="160" x2="760" y2="900">
          <stop offset="0" stop-color="var(--art-violet)"/>
          <stop offset="0.3" stop-color="var(--art-plum)"/>
          <stop offset="0.5" stop-color="var(--art-wine)"/>
          <stop offset="0.75" stop-color="var(--art-plum)"/>
          <stop offset="1" stop-color="var(--art-wine)"/>
        </linearGradient>
        <radialGradient id="artGlow" gradientUnits="userSpaceOnUse" cx="230" cy="620" r="330">
          <stop offset="0" stop-color="var(--art-teal)" stop-opacity="0.85"/>
          <stop offset="1" stop-color="var(--art-teal)" stop-opacity="0"/>
        </radialGradient>
        <linearGradient id="tailFill" gradientUnits="userSpaceOnUse" x1="150" y1="0" x2="760" y2="0">
          <stop offset="0" stop-color="var(--art-navy)"/>
          <stop offset="0.5" stop-color="var(--art-plum)"/>
          <stop offset="1" stop-color="var(--art-navy)"/>
        </linearGradient>
      </defs>

      <text class="title-lead" x="450" y="125" text-anchor="middle" font-size="72" letter-spacing="14">THE</text>

      <g class="title-block">
        <g fill="url(#artFill)">
          <text x="147" y="421" font-size="385" textLength="620" lengthAdjust="spacingAndGlyphs">LIN</text>
          <text x="147" y="755" font-size="385" textLength="620" lengthAdjust="spacingAndGlyphs" dy="0">DEN</text>
          <text x="147" y="882" font-size="171" textLength="620" lengthAdjust="spacingAndGlyphs">MOOR</text>
        </g>
        <g fill="url(#artGlow)">
          <text x="147" y="421" font-size="385" textLength="620" lengthAdjust="spacingAndGlyphs" aria-hidden="true">LIN</text>
          <text x="147" y="755" font-size="385" textLength="620" lengthAdjust="spacingAndGlyphs" aria-hidden="true">DEN</text>
          <text x="147" y="882" font-size="171" textLength="620" lengthAdjust="spacingAndGlyphs" aria-hidden="true">MOOR</text>
        </g>
      </g>

      <text class="title-tail" x="150" y="987" font-size="100" fill="url(#tailFill)" textLength="610" lengthAdjust="spacingAndGlyphs">COMPASS</text>
    </svg>

    <p class="author-line"><span class="author-with">WITH</span><span class="author-name">MARISA QUELL DARNBY</span></p>
  </main>
</body>
</html>
```